Business Card Design - Furniture Retail

Open to both Single or double sided design

We are launching a online ecommerce store that sells Scandinavian/Danish style of furniture in Australia.

We aspire to provide stylish but classic and designers' selection of furniture to the Australia public at affordable price. For the style of the furniture we are selling, please see the following links:

https://www.boxlyshare.com/sh/qrk7vz2mwpl04tn/BBXTpeLr3h52Kd7nWqYzRsGmu?dl=0

The style of the design we are looking for is clean, simple that look Scandinavian/Danish but yet it is timeless classic.

Aspiring Design
http://www.hallwick.com
http://brenlowe.com.au/
http://kolvo.furniture/
http://www.tipo.com/
Updates

Please display the card on normal angle for both front and back instead of funny angle. Please keep it display when displaying the design of the business cards so that we can focus on the designs rather than being confused by the unnecessary stuffs like the hands or background

I think there is already enough curve line on the logo itself so anything extra of the curve on the business card would be really unnecessary. Please avoid using any of the extra curve line on the business card, other than the logo itself. Thanks

Regular card and give them a matt celloglaze to create texture on card that makes it looked luxury and expensive.

Please display design on normal angle! Please only use white colour in the background (not the business card but the referring to the submission) rather than anything fancy so that we can focus on the design.

Target Market(s)

High end market consumers who are financially capable and who has good taste and appreciate good design

aged between 28 - 45 white collars professional/businessmen who live in metropolitan areas

Industry/Entity Type

Business

Font styles to use
Serif
Sans Serif

Requirements
Must have
• Regular card and give them a matt celloglaze to create texture on card that makes it looked luxury and expensive.

Please use the logo from the uploaded files

Company Name: Miles Orveda
Name: Peter Holm
Phone: +614 27 505 316
Website: www.milesorveda.com.au
Email: peter@milesorveda.com.au
Nice to have
• Colour is not limited to black and white
Should not have
• The concept photos of the furniture should NOT be used in the FRONT page of the business card.

```html
<!DOCTYPE html>
<html lang="en">
<head>
<meta charset="utf-8">
<title>Miles Orveda — Business Cards</title>
<link rel="stylesheet" href="https://fonts.googleapis.com/css2?family=Tinos&family=Arimo&display=swap">
<style>
  :root {
    --page-bg: #ffffff;
    --card-dark: #0b0b0b;
    --card-dark-grain-a: #141414;
    --card-dark-grain-b: #050505;
    --card-light: #ffffff;
    --card-border: #8a8a8a;
    --ink-dark: #111111;
    --ink-light: #f4f4f4;
  }
  * { box-sizing: border-box; margin: 0; padding: 0; }
  html, body {
    width: 1200px;
    height: 1200px;
    overflow: hidden;
    background: var(--page-bg);
  }
  .sheet {
    position: relative;
    width: 1200px;
    height: 1200px;
  }
  .card {
    position: absolute;
    width: 400px;
    height: 400px;
    overflow: hidden;
  }
  .card--tl { left: 175px; top: 175px; }
  .card--tr { left: 625px; top: 175px; }
  .card--bl { left: 175px; top: 625px; }
  .card--br { left: 625px; top: 625px; }

  .card--dark { background: var(--card-dark); color: var(--ink-light); }
  .card--light {
    background: var(--card-light);
    color: var(--ink-dark);
    border: 1px solid var(--card-border);
  }
  .card__texture {
    position: absolute;
    inset: 0;
    background: linear-gradient(180deg, var(--card-dark-grain-a) 0%, var(--card-dark-grain-b) 45%, var(--card-dark-grain-a) 70%, var(--card-dark-grain-b) 100%);
  }
  .card__content {
    position: relative;
    width: 100%;
    height: 100%;
  }
  .brand-name {
    position: absolute;
    left: 0;
    right: 0;
    text-align: center;
    font-family: "Tinos", "Times New Roman", serif;
    font-size: 25px;
    letter-spacing: 1px;
    text-transform: uppercase;
    line-height: 1;
  }
  .card--front .brand-name { top: 188px; }
  .card--back .brand-name { top: 119px; }

  .contact {
    position: absolute;
    left: 0;
    right: 0;
    text-align: center;
  }
  .contact__name {
    top: 192px;
    font-family: "Tinos", "Times New Roman", serif;
    font-size: 18px;
  }
  .contact__phone {
    top: 236px;
    font-family: "Arimo", Arial, sans-serif;
    font-size: 13px;
  }
  .contact__links {
    top: 265px;
    font-family: "Arimo", Arial, sans-serif;
    font-size: 10px;
    line-height: 12px;
  }
</style>
</head>
<body>
<main class="sheet">

  <section class="card card--dark card--front card--tl">
    <div class="card__texture" role="img" aria-label="Dark woodgrain card texture"></div>
    <div class="card__content">
      <p class="brand-name">Miles Orveda</p>
    </div>
  </section>

  <section class="card card--light card--front card--tr">
    <div class="card__content">
      <p class="brand-name">Miles Orveda</p>
    </div>
  </section>

  <section class="card card--light card--back card--bl">
    <div class="card__content">
      <p class="brand-name">Miles Orveda</p>
      <p class="contact contact__name">Peter Holm</p>
      <p class="contact contact__phone">+614 27 505 316</p>
      <p class="contact contact__links">www.milesorveda.com.au<br>peter@milesorveda.com.au</p>
    </div>
  </section>

  <section class="card card--dark card--back card--br">
    <div class="card__texture" role="img" aria-label="Dark woodgrain card texture"></div>
    <div class="card__content">
      <p class="brand-name">Miles Orveda</p>
      <p class="contact contact__name">Peter Holm</p>
      <p class="contact contact__phone">+614 27 505 316</p>
      <p class="contact contact__links">www.milesorveda.com.au<br>peter@milesorveda.com.au</p>
    </div>
  </section>

</main>
</body>
</html>
```